角2、長3、長3窓付きの封筒デザインをお願い致します。
(長3は長3窓付きは共通のデザインで良いです。)
封筒は白を予定しています。
ハレヤカサービスモリオ
〒940-0817 新潟県長岡市西川端2-8-4
TEL 090-5187-2940 FAX 0258-39-1862
青系、緑系
ロゴの添付ファイルあり
印刷通販のミツバプリで封筒印刷(刷込)を予定。

ロゴと社名、アドレス、そして封筒のデザインに対して
封筒の余白のバランスが自分のイメージに合っていたと思います。

さすがプロのデザイナーだけあってそれぞれ素晴らしい提案で
選考するのが大変でした。
提案して頂いたワークナーの皆様ありがとうございました。

```html
<!DOCTYPE html>
<html lang="ja">
<head>
<meta charset="utf-8">
<title>ハレヤカサービスモリオ 封筒デザイン</title>
<link rel="stylesheet" href="https://fonts.googleapis.com/css2?family=Noto+Sans+JP:wght@400;500;700&display=swap">
<style>
  :root {
    --paper: #ffffff;
    --edge: #b9bcc0;
    --shade: #e9ebee;
    --ink: #333a40;
    --brand-blue: #1f6fb8;
    --mist-light: #eef6fc;
    --mist: #cfe4f4;
    --divider: #9aa3ab;
  }
  * { margin: 0; padding: 0; box-sizing: border-box; }
  html, body { width: 1200px; height: 2925px; overflow: hidden; background: var(--paper); }
  body { position: relative; font-family: "Noto Sans JP", sans-serif; color: var(--ink); }

  .spec-note {
    position: absolute; left: 96px; font-size: 15px; letter-spacing: 0.02em; white-space: nowrap;
  }
  .spec-note .plan { font-size: 22px; margin-right: 24px; }

  .envelope { position: absolute; left: 0; width: 1200px; }
  .envelope > svg.body { position: absolute; inset: 0; }

  .brand { position: absolute; display: flex; align-items: center; }
  .brand-mark {
    width: 86px; height: 86px; border-radius: 50%;
    background: var(--brand-blue); flex: none; margin-right: 50px;
  }
  .brand-name {
    font-size: 30px; font-weight: 500; line-height: 1.15; color: var(--brand-blue);
    width: 160px; flex: none;
  }
  .brand-divider { width: 2px; height: 86px; background: var(--divider); margin: 0 20px 0 24px; flex: none; }
  .contact { white-space: nowrap; }
  .contact .company { font-size: 29px; font-weight: 700; color: var(--brand-blue); line-height: 1.3; letter-spacing: 0.02em; }
  .contact .line { font-size: 17px; line-height: 1.55; color: var(--ink); }

  .decoration-area {
    position: absolute; border-radius: 8px;
    background: linear-gradient(160deg, var(--mist-light) 0%, var(--mist) 100%);
  }
</style>
</head>
<body>

  <!-- 角2 -->
  <section class="envelope kaku2" style="top:0;height:1700px">
    <svg class="body" width="1200" height="1700" viewBox="0 0 1200 1700">
      <path d="M21 192 L60 21 L1135 21 L1173 192 Z" fill="var(--shade)" stroke="var(--edge)" stroke-width="2"/>
      <rect x="21" y="192" width="1152" height="1475" fill="var(--paper)" stroke="var(--edge)" stroke-width="2"/>
    </svg>
    <p class="spec-note" style="top:230px"><span class="plan">A</span>CMYK4色　（刷込ではなく普通の封筒印刷／グラデーション・アミあり）　ゴシック体に変更済み</p>
    <div class="decoration-area" role="img" aria-label="ブランドの装飾イラスト" style="left:820px;top:1320px;width:250px;height:240px"></div>
    <div class="brand" style="left:112px;top:1420px">
      <div class="brand-mark"></div>
      <div class="brand-name">Hareyaka<br>Morio</div>
      <div class="brand-divider"></div>
      <div class="contact">
        <p class="company">ハレヤカサービスモリオ</p>
        <p class="line">〒940-0817 新潟県長岡市西川端2-8-4</p>
        <p class="line">TEL 090-5187-2940　FAX 0258-39-1862</p>
      </div>
    </div>
  </section>

  <!-- 長3 -->
  <p class="spec-note" style="top:1700px"><span class="plan">A</span>CMYK4色　（刷込ではなく普通の封筒印刷／グラデーション・アミあり）　ゴシック体に変更済み</p>
  <section class="envelope naga3" style="top:1752px;height:540px">
    <svg class="body" width="1200" height="540" viewBox="0 0 1200 540">
      <path d="M1067 0 L1173 20 L1173 513 L1067 533 Z" fill="var(--shade)" stroke="var(--edge)" stroke-width="2"/>
      <rect x="21" y="0" width="1046" height="533" fill="var(--paper)" stroke="var(--edge)" stroke-width="2"/>
    </svg>
    <div class="decoration-area" role="img" aria-label="ブランドの装飾イラスト" style="left:790px;top:280px;width:250px;height:220px"></div>
    <div class="brand" style="left:112px;top:360px">
      <div class="brand-mark"></div>
      <div class="brand-name">Hareyaka<br>Morio</div>
      <div class="brand-divider"></div>
      <div class="contact">
        <p class="company">ハレヤカサービスモリオ</p>
        <p class="line">〒940-0817 新潟県長岡市西川端2-8-4</p>
        <p class="line">TEL 090-5187-2940　FAX 0258-39-1862</p>
      </div>
    </div>
  </section>

  <!-- 長3 窓付き -->
  <p class="spec-note" style="top:2318px"><span class="plan">A</span>CMYK4色　（刷込ではなく普通の封筒印刷／グラデーション・アミあり）　ゴシック体に修正済み</p>
  <section class="envelope naga3-window" style="top:2368px;height:540px">
    <svg class="body" width="1200" height="540" viewBox="0 0 1200 540">
      <path d="M1067 0 L1173 20 L1173 513 L1067 533 Z" fill="var(--shade)" stroke="var(--edge)" stroke-width="2"/>
      <rect x="21" y="0" width="1046" height="533" fill="var(--paper)" stroke="var(--edge)" stroke-width="2"/>
      <rect x="112" y="40" width="429" height="219" rx="22" fill="var(--paper)" stroke="var(--edge)" stroke-width="3"/>
    </svg>
    <div class="decoration-area" role="img" aria-label="ブランドの装飾イラスト" style="left:790px;top:280px;width:250px;height:220px"></div>
    <div class="brand" style="left:112px;top:360px">
      <div class="brand-mark"></div>
      <div class="brand-name">Hareyaka<br>Morio</div>
      <div class="brand-divider"></div>
      <div class="contact">
        <p class="company">ハレヤカサービスモリオ</p>
        <p class="line">〒940-0817 新潟県長岡市西川端2-8-4</p>
        <p class="line">TEL 090-5187-2940　FAX 0258-39-1862</p>
      </div>
    </div>
  </section>

</body>
</html>
```